Torvique Blister Pack Graphic

Design a print quality graphic foe insertion in blister packaging
based on the attached design Must be print ready
Template attached
Two sided print ...identical on both sides
DO NOT INCLUDE'54,000 hr 10 yr guarantee" from sample
DO NOT INCLUDE "free velquarrin" from attached sample

Create new graphic for single bulb blister pack based previous on bulb and velquarrin pack

Target Market(s)

Torvique end users

Industry/Entity Type

Lighting Fixture

Font styles to use
Sans Serif

Colors
faa54b

Requirements
Must have
• Immediate eye appeal

```html
<!DOCTYPE html>
<html lang="en">
<head>
<meta charset="utf-8">
<title>Torvique Blister Pack Insert</title>
<link rel="stylesheet" href="https://fonts.googleapis.com/css2?family=Roboto:wght@400;500;700&display=swap">
<style>
  :root {
    --page: #ffffff;
    --ink: #0b0909;
    --gold: #f7d70f;
    --ember: #f0502f;
    --maroon: #6b1220;
    --crimson: #c8202a;
    --flame-orange: #faa54b;
    --bulb: #ffffff;
    --outline: #111111;
  }
  * { margin: 0; padding: 0; box-sizing: border-box; }
  html, body {
    width: 1200px; height: 1200px; overflow: hidden;
    background: var(--page);
    font-family: "Roboto", Arial, sans-serif;
  }
  .canvas { position: relative; width: 1200px; height: 1200px; }
  .card {
    position: absolute; left: 369px; top: 166px;
    width: 452px; height: 861px; background: var(--ink);
  }
  .artwork { position: absolute; left: 0; top: 0; }
  .brand-name {
    position: absolute; left: 391px; width: 408px; top: 282px;
    text-align: center; font-size: 38px; font-weight: 400;
    letter-spacing: 1px; color: var(--ember); line-height: 1;
  }
  .headline {
    position: absolute; left: 391px; width: 408px; top: 416px;
    text-align: center; font-size: 23px; font-weight: 500; color: var(--gold);
  }
  .badge-label {
    position: absolute; width: 94px; text-align: center;
    font-size: 23px; font-weight: 500; color: #ffffff; line-height: 1;
  }
  .badge-label.led { left: 421px; top: 512px; }
  .badge-label.voltage { left: 676px; top: 512px; }
  .feature {
    position: absolute; width: 120px; text-align: center;
    color: var(--gold); font-weight: 700; line-height: 1.15;
  }
  .feature .big { display: block; font-size: 21px; }
  .feature .small { display: block; font-size: 17px; font-weight: 500; }
  .feature.listing { left: 408px; top: 591px; }
  .feature.lifetime { left: 669px; top: 591px; }
  .web-address {
    position: absolute; left: 391px; width: 408px; top: 954px;
    text-align: center; font-size: 17px; font-weight: 700;
    letter-spacing: 1px; color: var(--ink);
  }
</style>
</head>
<body>
<div class="canvas">
  <div class="card"></div>

  <svg class="artwork" width="1200" height="1200" viewBox="0 0 1200 1200">
    <defs>
      <linearGradient id="panelShade" x1="0" y1="0" x2="0" y2="1">
        <stop offset="0" stop-color="#0b0909"/>
        <stop offset="0.3" stop-color="#140a0b"/>
        <stop offset="0.55" stop-color="#5a101c"/>
        <stop offset="0.75" stop-color="#8a1824"/>
        <stop offset="1" stop-color="#c8202a"/>
      </linearGradient>
      <linearGradient id="fireTones" x1="0" y1="0" x2="0" y2="1">
        <stop offset="0" stop-color="#c8202a" stop-opacity="0"/>
        <stop offset="0.35" stop-color="#e8432c"/>
        <stop offset="0.7" stop-color="#faa54b"/>
        <stop offset="1" stop-color="#f7d70f"/>
      </linearGradient>
      <radialGradient id="badgeGlow" cx="0.5" cy="0.5" r="0.5">
        <stop offset="0" stop-color="#ff3b3b"/>
        <stop offset="0.6" stop-color="#b0141e"/>
        <stop offset="1" stop-color="#5a0a14"/>
      </radialGradient>
    </defs>

    <!-- frame -->
    <rect class="frame" x="394.5" y="192.5" width="401" height="807" fill="url(#panelShade)" stroke="var(--gold)" stroke-width="7"/>

    <!-- swoosh bands -->
    <path class="band-gold" d="M398,292 C450,372 560,388 650,358 C720,334 760,326 792,334 L792,304 C740,296 680,316 620,338 C540,362 450,352 398,262 Z" fill="var(--gold)"/>
    <path class="band-ember" d="M398,368 C470,398 560,400 650,380 C720,364 770,378 792,432 L792,398 C760,360 700,352 640,366 C560,384 470,388 398,356 Z" fill="var(--ember)"/>

    <!-- fire area -->
    <rect class="fire-area" x="398" y="700" width="394" height="296" fill="url(#fireTones)" role="img" aria-label="Illustrated flames rising across the lower panel"/>

    <!-- badges -->
    <circle cx="468" cy="524" r="46" fill="url(#badgeGlow)" stroke="var(--gold)" stroke-width="3"/>
    <circle cx="723" cy="524" r="46" fill="url(#badgeGlow)" stroke="var(--gold)" stroke-width="3"/>

    <!-- bulb area -->
    <rect class="bulb-area" x="511" y="459" width="169" height="455" rx="84" fill="var(--bulb)" stroke="var(--outline)" stroke-width="2" role="img" aria-label="Candle-shaped LED flame bulb with screw base"/>
  </svg>

  <div class="brand-name">TORVIQUE</div>
  <div class="headline">World's Best Flame Bulb</div>
  <div class="badge-label led">LED</div>
  <div class="badge-label voltage">120V</div>
  <div class="feature listing"><span class="big">QVL</span><span class="small">listed</span></div>
  <div class="feature lifetime"><span class="big">30,000</span><span class="small">Hours</span></div>
  <div class="web-address">www.torvique.com</div>
</div>
</body>
</html>
```